Business card for Chiropractic clinics needs reworked / redesigned

The business card in attachment was designed 10 years ago. It is in need of an update.
We have 2 clinics:
VELDHOVE KLINIEK & VELDHOVE KLINIEK NOORD
Only one address needs to be on the card for doctors that only work in one clinic and two addresses need to be on the card for the doctors that work in both clinics.

Target Market(s)

patients/referrers

Industry/Entity Type

Medical

Contact Information for Business Card

Logo (in full or zoomed-in)
Clinic Name
Doctor name and title
clinic address, website, tel, email

Font styles to use
Sans Serif

Colors

Designer to choose colors to be used in the design.

Requirements
Must have
• Good contrast/readability
• We like modern minimalistic designs
• The Bcard needs to project our very high standard of proficiency/professionalism
Should not have
• Not curly
• Not to much colours

```html
<!DOCTYPE html>
<html lang="nl">
<head>
<meta charset="utf-8">
<title>Veldhove Kliniek – Business Card</title>
<link rel="stylesheet" href="https://fonts.googleapis.com/css2?family=Montserrat:wght@400;500;600&display=swap">
<style>
  :root {
    --ink: #0b2426;
    --paper: #ffffff;
    --muted: #6b7577;
    --backdrop: #3a3a3a;
    --mark: #0b2426;
  }
  * { margin: 0; padding: 0; box-sizing: border-box; }
  html, body {
    width: 1200px; height: 960px; overflow: hidden;
    background: var(--backdrop);
    font-family: "Montserrat", sans-serif;
  }
  .canvas { position: relative; width: 1200px; height: 960px; }

  .card {
    position: absolute; left: 281px; width: 655px; height: 373px;
    border-radius: 20px; overflow: hidden;
  }
  .card--front { top: 80px; background: var(--paper); }
  .card--back { top: 506px; background: var(--ink); }

  /* front */
  .clinic-mark {
    position: absolute; left: 61px; top: 110px;
    display: flex; align-items: center; gap: 10px;
  }
  .clinic-mark__dot { width: 14px; height: 14px; border-radius: 50%; background: var(--mark); }
  .clinic-mark__name {
    font-size: 11px; font-weight: 600; line-height: 1.3;
    letter-spacing: 0.06em; color: var(--ink);
  }
  .person { position: absolute; left: 168px; top: 106px; }
  .person__name { font-size: 22px; font-weight: 600; color: var(--ink); letter-spacing: 0.01em; }
  .person__title { margin-top: 4px; font-size: 16px; font-weight: 400; color: var(--muted); }

  .contact-band {
    position: absolute; left: 0; right: 0; bottom: 0; height: 124px;
    background: var(--ink); color: var(--paper);
  }
  .contact-list { position: absolute; left: 61px; top: 26px; list-style: none; }
  .contact-list li {
    display: flex; align-items: center; gap: 8px;
    height: 22px; font-size: 14px; font-weight: 400;
  }
  .contact-list svg { width: 10px; height: 10px; flex: none; }
  .address { position: absolute; left: 446px; top: 28px; display: flex; gap: 8px; }
  .address svg { width: 10px; height: 14px; margin-top: 3px; flex: none; }
  .address p { font-size: 14px; line-height: 22px; font-weight: 400; }

  /* back */
  .back-mark {
    position: absolute; left: 165px; top: 168px;
    width: 36px; height: 36px; background: var(--paper);
  }
  .brand { position: absolute; left: 290px; top: 155px; width: 200px; text-align: center; }
  .brand__name { font-size: 24px; font-weight: 600; color: var(--paper); white-space: nowrap; margin-left: -60px; margin-right: -60px; }
  .brand__web { margin-top: 4px; font-size: 14px; color: var(--paper); }
</style>
</head>
<body>
<main class="canvas">

  <section class="card card--front" aria-label="Card front">
    <div class="clinic-mark">
      <span class="clinic-mark__dot"></span>
      <span class="clinic-mark__name">VELDHOVE<br>KLINIEK</span>
    </div>
    <div class="person">
      <h1 class="person__name">ELIAS VERBEKE</h1>
      <p class="person__title">President &amp; CEO</p>
    </div>

    <div class="contact-band">
      <ul class="contact-list">
        <li>
          <svg viewBox="0 0 10 10"><path d="M2 1 L3.5 1 L4 3 L3 3.8 Q4 6 6.2 7 L7 6 L9 6.5 L9 8 Q8.5 9 7.5 9 Q1 8 1 2.5 Q1 1.3 2 1 Z" fill="#fff"/></svg>
          +32 9 555 01 48
        </li>
        <li>
          <svg viewBox="0 0 10 10"><rect x="0.5" y="2" width="9" height="6" fill="#fff"/><path d="M0.5 2 L5 5.5 L9.5 2" stroke="#0b2426" stroke-width="1" fill="none"/></svg>
          info@veldhovekliniek.be
        </li>
        <li>
          <svg viewBox="0 0 10 10" fill="none" stroke="#fff" stroke-width="0.9"><circle cx="5" cy="5" r="4.2"/><ellipse cx="5" cy="5" rx="1.8" ry="4.2"/><path d="M0.8 5 H9.2 M1.5 3 H8.5 M1.5 7 H8.5"/></svg>
          www.veldhovekliniek.be
        </li>
      </ul>
      <div class="address">
        <svg viewBox="0 0 10 14"><path d="M5 0 A5 5 0 0 1 10 5 C10 8 5 14 5 14 C5 14 0 8 0 5 A5 5 0 0 1 5 0 Z" fill="#fff"/><circle cx="5" cy="5" r="1.8" fill="#0b2426"/></svg>
        <p>VELDHOVE KLINIEK<br>Lindenlaan 48</p>
      </div>
    </div>
  </section>

  <section class="card card--back" aria-label="Card back">
    <span class="back-mark"></span>
    <div class="brand">
      <h2 class="brand__name">VELDHOVE KLINIEK</h2>
      <p class="brand__web">www.veldhovekliniek.be</p>
    </div>
  </section>

</main>
</body>
</html>
```